Brisk Hounds for dog food

its for dry dog food label that will be used for packaging. Two (2) labels for front and back.
In front it will have the brand of "Brisk Hounds" using graphics or pictures (photos) of Dogs, contain of wording super premium pet nutrition ; completed, balanced and quality nutrition ; hypo allergenic, grain free and spacing that can be switched among wording of 'chicken, beef, lamb, plus other variety.
on back it will have ingredients like common all dog food and having spaces that consist Protein..% ; Fat..% ; Fiber..% ; and moisture..% ; feeding suggestion that have standard suggestion for small breed to big dogs ; Also have US formula under licensed by ... ; net weight..kgs ; space for barcode and QR code
Updates
Target Market(s)
medium to high consumer
Colors
Designer to choose colors to be used in the design.
Requirements
Must have
- Completed, Balanced and Quality Nutrition, Hypo Allergenic
- "Chicken and Grain Free"
Nice to have
- the picture of puppy and adult dog (siberian husky)
- small and large Breed

```html
<!DOCTYPE html>
<html lang="en">
<head>
<meta charset="utf-8">
<title>Brisk Hounds – Front Label</title>
<link href="https://fonts.googleapis.com/css2?family=Libre+Baskerville:wght@700&family=Old+Standard+TT:wght@700&family=Open+Sans:wght@400&display=swap" rel="stylesheet">
<style>
  :root {
    --page-bg: #dcdcdc;
    --label-white: #f7f7f7;
    --label-pale: #ececec;
    --ink-dark: #333131;
    --band-dark: #3b3a3a;
    --accent-orange: #f2a431;
    --badge-red: #d4212a;
    --text-light: #ffffff;
    --fur-gold: #c99a55;
    --fur-light: #e2c28c;
    --rooster-taupe: #8c7b67;
  }
  html, body {
    margin: 0;
    padding: 0;
    width: 1200px;
    height: 930px;
    overflow: hidden;
    background: var(--page-bg);
  }
  .front-label {
    position: absolute;
    left: 300px;
    top: 15px;
    width: 600px;
    height: 900px;
    display: block;
    box-shadow: 0 6px 18px rgba(0,0,0,0.25);
  }
  .brand-name {
    font-family: "Libre Baskerville", serif;
    font-weight: 700;
    fill: var(--ink-dark);
  }
  .ribbon-title {
    font-family: "Old Standard TT", serif;
    font-weight: 700;
    fill: var(--ink-dark);
    font-size: 42px;
  }
  .claim-text {
    font-family: "Open Sans", sans-serif;
    font-weight: 400;
    fill: var(--text-light);
    font-size: 18px;
  }
  .badge-text {
    font-family: "Old Standard TT", serif;
    font-weight: 700;
    fill: var(--text-light);
    font-size: 22px;
  }
  .flavour-text {
    font-family: "Old Standard TT", serif;
    font-weight: 700;
    fill: var(--text-light);
    font-size: 48px;
  }
</style>
</head>
<body>
<svg class="front-label" viewBox="0 0 600 900" xmlns="http://www.w3.org/2000/svg">
  <defs>
    <linearGradient id="label-surface" x1="0" y1="0" x2="1" y2="1">
      <stop offset="0" stop-color="var(--label-white)"/>
      <stop offset="1" stop-color="var(--label-pale)"/>
    </linearGradient>
    <radialGradient id="dog-tones" cx="0.5" cy="0.4" r="0.7">
      <stop offset="0" stop-color="var(--fur-light)"/>
      <stop offset="1" stop-color="var(--fur-gold)"/>
    </radialGradient>
    <linearGradient id="rooster-tones" x1="0" y1="0" x2="0" y2="1">
      <stop offset="0" stop-color="var(--rooster-taupe)" stop-opacity="0.75"/>
      <stop offset="1" stop-color="var(--rooster-taupe)"/>
    </linearGradient>
    <linearGradient id="ribbon-fade" x1="0" y1="0" x2="1" y2="0">
      <stop offset="0" stop-color="var(--accent-orange)" stop-opacity="0"/>
      <stop offset="0.25" stop-color="var(--accent-orange)" stop-opacity="0.85"/>
      <stop offset="1" stop-color="var(--accent-orange)"/>
    </linearGradient>
  </defs>

  <!-- label surface -->
  <rect class="label-surface" x="0" y="0" width="600" height="900" fill="url(#label-surface)"/>

  <!-- brand -->
  <circle class="brand-dot" cx="458" cy="150" r="56" fill="var(--ink-dark)"/>
  <text class="brand-name" x="97" y="287" font-size="112">Brisk</text>
  <text class="brand-name" x="192" y="362" font-size="66" textLength="260" lengthAdjust="spacingAndGlyphs">Hounds</text>

  <!-- dog photograph area -->
  <rect class="dog-photo" role="img" aria-label="Photo of a smiling golden retriever"
        x="0" y="386" width="280" height="360" fill="url(#dog-tones)"/>

  <!-- orange swoosh and dark base -->
  <path class="accent-swoosh" d="M0,722 C250,702 490,612 600,440 L600,470 C500,640 250,730 0,742 Z" fill="var(--accent-orange)"/>
  <path class="base-band" d="M0,740 C250,728 500,640 600,468 L600,900 L0,900 Z" fill="var(--band-dark)"/>

  <!-- ribbon headline -->
  <rect class="headline-ribbon" x="165" y="591" width="435" height="92" fill="url(#ribbon-fade)"/>
  <text class="ribbon-title" x="582" y="634" text-anchor="end" textLength="375" lengthAdjust="spacingAndGlyphs">SUPER PREMIUM</text>
  <text class="ribbon-title" x="582" y="676" text-anchor="end" textLength="345" lengthAdjust="spacingAndGlyphs">PET NUTRITION</text>

  <!-- nutrition claim -->
  <text class="claim-text" x="582" y="706" text-anchor="end">Completed, Balanced and</text>
  <text class="claim-text" x="582" y="729" text-anchor="end">Quality Nutrition, Hypo Allergenic</text>

  <!-- rooster illustration area -->
  <rect class="rooster-art" role="img" aria-label="Silhouette illustration of a rooster"
        x="445" y="740" width="155" height="160" fill="url(#rooster-tones)"/>

  <!-- breed badge -->
  <polygon class="breed-badge" fill="var(--badge-red)"
    points="87,627 98,645 116,632 120,653 141,648 136,669 156,674 143,690 159,704 139,712 147,732 126,732 125,754 106,745 98,765 87,748 76,765 68,745 49,754 48,732 27,732 35,712 15,704 31,690 18,674 38,669 33,648 54,653 58,632 76,645"/>
  <g class="badge-label" transform="rotate(-22 87 695)">
    <text class="badge-text" x="87" y="691" text-anchor="middle">LARGE</text>
    <text class="badge-text" x="87" y="715" text-anchor="middle">BREED</text>
  </g>

  <!-- flavour -->
  <text class="flavour-text" x="46" y="820" textLength="352" lengthAdjust="spacingAndGlyphs">CHICKEN AND</text>
  <text class="flavour-text" x="46" y="864" textLength="315" lengthAdjust="spacingAndGlyphs">GRAIN FREE</text>
</svg>
</body>
</html>
```